New Business Card for Innovative Tool Company

We need a new design of business card for our florida based tool manufacturing company. I will attach 2 files that we use for our logo, use whichever you feel works best for the card. Main colours are as per logo, and we can use different shades of black/white/grey for the background.

Contact Information for Business Card

Name/Jobtitle/cell
Brackwell Tools
Suite 214c
3190 Harlowmere Pkw
Fenmore, FL34720
USA
name@brackwellco.example
www.brackwellco.example

Font styles to use
Sans Serif

Colors

Designer to choose colors to be used in the design.

Requirements
Must have
• Icons for Chatterly, Quiplet, Snapvista, Findora & Viewtube

```html
<!DOCTYPE html>
<html lang="en">
<head>
<meta charset="utf-8">
<title>Brackwell Tools — Business Card</title>
<link href="https://fonts.googleapis.com/css2?family=Montserrat:wght@400;500;700;800&display=swap" rel="stylesheet">
<style>
  :root {
    --backdrop: #3a3a3a;
    --card-black: #1c1c1c;
    --card-black-deep: #141414;
    --gloss: #2e2e2e;
    --gloss-edge: #3c3c3c;
    --accent: #f2ea2e;
    --ink-light: #f1f1f1;
  }
  * { box-sizing: border-box; margin: 0; padding: 0; }
  html, body { width: 1200px; height: 868px; overflow: hidden; }
  body {
    background: var(--backdrop);
    font-family: "Montserrat", Arial, sans-serif;
    display: flex;
    align-items: center;
    justify-content: center;
    gap: 40px;
  }
  .card {
    position: relative;
    width: 520px;
    height: 297px;
    border-radius: 4px;
    overflow: hidden;
    box-shadow: 0 14px 30px rgba(0,0,0,0.45);
  }

  /* Back side: tone-on-tone spot gloss */
  .card--back {
    background: var(--card-black-deep);
    display: flex;
    flex-direction: column;
    align-items: center;
    justify-content: center;
    gap: 26px;
  }
  .brand-lockup {
    display: flex;
    align-items: center;
    gap: 14px;
  }
  .brand-lockup__mark {
    width: 40px; height: 40px;
    border-radius: 50%;
    border: 2px solid var(--gloss-edge);
  }
  .brand-lockup__name {
    font-weight: 800;
    font-size: 34px;
    letter-spacing: 2px;
    color: var(--gloss);
    text-transform: uppercase;
  }
  .social-row {
    display: flex;
    gap: 12px;
    list-style: none;
  }
  .social-row__item {
    width: 24px; height: 24px;
    border-radius: 50%;
    border: 1.5px solid var(--gloss-edge);
  }

  /* Front side: contact details */
  .card--front { background: var(--card-black); }
  .front__brand {
    position: absolute;
    top: 30px; right: 40px;
    font-weight: 800;
    font-size: 30px;
    letter-spacing: 2px;
    color: var(--accent);
    text-transform: uppercase;
  }
  .front__person {
    position: absolute;
    top: 92px; left: 30px;
  }
  .person__name {
    font-weight: 700;
    font-size: 19px;
    color: var(--accent);
  }
  .person__title {
    font-size: 12px;
    color: var(--ink-light);
    margin-top: 2px;
  }
  .contact-list {
    position: absolute;
    top: 150px; left: 30px;
    list-style: none;
    font-size: 12.5px;
    color: var(--ink-light);
    line-height: 19px;
  }
  .contact-list__item { display: flex; align-items: center; gap: 8px; }
  .contact-list__icon { width: 13px; height: 13px; flex: none; }
  .address {
    position: absolute;
    top: 218px; left: 30px;
    font-style: normal;
    font-size: 12.5px;
    color: var(--ink-light);
    line-height: 18px;
  }
  .front__arc {
    position: absolute;
    right: -110px; bottom: -120px;
    width: 330px; height: 330px;
  }
</style>
</head>
<body>

  <section class="card card--back" aria-label="Card back">
    <div class="brand-lockup">
      <span class="brand-lockup__mark"></span>
      <span class="brand-lockup__name">Brackwell Tools</span>
    </div>
    <ul class="social-row" aria-label="Social channels">
      <li class="social-row__item" aria-label="Chatterly"></li>
      <li class="social-row__item" aria-label="Quiplet"></li>
      <li class="social-row__item" aria-label="Findora"></li>
      <li class="social-row__item" aria-label="Snapvista"></li>
      <li class="social-row__item" aria-label="Viewtube"></li>
    </ul>
  </section>

  <section class="card card--front" aria-label="Card front">
    <div class="front__brand">Brackwell Tools</div>

    <div class="front__person">
      <div class="person__name">Dorian PELLEY</div>
      <div class="person__title">Managing Director</div>
    </div>

    <ul class="contact-list">
      <li class="contact-list__item">
        <svg class="contact-list__icon" viewBox="0 0 16 16"><path d="M3 1.5l3 .5 1 3.5-2 1.2a9 9 0 0 0 4.3 4.3l1.2-2 3.5 1 .5 3c-7 1.5-13-4.5-11.5-11.5z" fill="#f2ea2e"/></svg>
        000 000 0000
      </li>
      <li class="contact-list__item">
        <svg class="contact-list__icon" viewBox="0 0 16 16"><rect x="1" y="3" width="14" height="10" fill="none" stroke="#f2ea2e" stroke-width="1.4"/><path d="M1 3l7 6 7-6" fill="none" stroke="#f2ea2e" stroke-width="1.4"/></svg>
        name@brackwellco.example
      </li>
      <li class="contact-list__item">
        <svg class="contact-list__icon" viewBox="0 0 16 16"><g fill="none" stroke="#f2ea2e" stroke-width="1.3"><circle cx="8" cy="8" r="6.5"/><ellipse cx="8" cy="8" rx="3" ry="6.5"/><path d="M1.5 8h13M2.5 4.5h11M2.5 11.5h11"/></g></svg>
        www.brackwellco.example
      </li>
    </ul>

    <address class="address">
      Suite 214c, 3190 Harlowmere Pkw<br>
      Fenmore, FL34720, USA
    </address>

    <svg class="front__arc" viewBox="0 0 330 330" aria-hidden="true">
      <circle cx="165" cy="165" r="160" fill="none" stroke="#f2ea2e" stroke-width="3"/>
    </svg>
  </section>

</body>
</html>
```